Lena Marwick Biz Card
biz card and stationary
Lena Marwick Biz Card - Financial Services
Creative Brief
Bright & Fun-filled
Lena Marwick
Independent Agent
Charlotte, NC
Lenamarwick@quillpost.example
www.marwickInsurance.example
Please use the head shot attached and the logo.
I will be uploading an example of content for the back of their card. please use that information.

```html
<!DOCTYPE html>
<html lang="en">
<head>
<meta charset="utf-8">
<title>Lena Marwick Business Card</title>
<link rel="stylesheet" href="https://fonts.googleapis.com/css2?family=Open+Sans:wght@400;600;700&family=Tinos:wght@400;700&display=swap">
<style>
  :root {
    --page-bg: #d9dadc;
    --card-white: #ffffff;
    --navy: #1f2a8a;
    --royal: #2b3cae;
    --blue-deep: #141c6a;
    --green: #5cb82e;
    --ink: #3a3a3a;
    --ink-soft: #6b6b6b;
    --photo-warm: #c9a987;
    --photo-dark: #2b2b2b;
  }
  * { box-sizing: border-box; margin: 0; padding: 0; }
  html, body { width: 1200px; height: 874px; overflow: hidden; }
  body {
    background: var(--page-bg);
    display: flex;
    align-items: center;
    justify-content: center;
    gap: 60px;
    font-family: "Open Sans", Arial, sans-serif;
  }
  .card {
    position: relative;
    width: 520px;
    height: 297px;
    background: var(--card-white);
    overflow: hidden;
    box-shadow: 0 10px 28px rgba(0,0,0,0.25);
  }
  .card-art { position: absolute; inset: 0; }

  /* front */
  .front .headshot {
    position: absolute;
    left: 0; top: 0;
    width: 520px; height: 130px;
  }
  .front .brand {
    position: absolute;
    left: 30px; top: 168px;
    display: flex; align-items: center; gap: 8px;
    font-family: "Open Sans", Arial, sans-serif;
    font-weight: 700; font-size: 19px;
    color: var(--navy);
  }
  .brand .mark-dot {
    width: 16px; height: 16px; border-radius: 50%;
    background: var(--green);
  }
  .front .agent {
    position: absolute; left: 30px; bottom: 30px;
  }
  .agent .name {
    font-family: "Tinos", "Times New Roman", serif;
    font-size: 17px; letter-spacing: 1px;
    color: var(--ink); text-transform: uppercase;
  }
  .agent .title {
    font-size: 10px; color: var(--ink-soft); margin-top: 2px;
  }
  .front .contact {
    position: absolute; right: 28px; bottom: 30px;
    text-align: left; font-size: 10.5px; line-height: 1.55;
    color: var(--ink);
  }
  .front .accent-tab {
    position: absolute; left: 0; bottom: 0;
    width: 120px; height: 5px; background: var(--green);
  }

  /* back */
  .back .brand {
    position: absolute; left: 34px; top: 126px;
    display: flex; align-items: center; gap: 8px;
    font-weight: 700; font-size: 18px; color: var(--navy);
  }
  .back .services {
    position: absolute; left: 232px; top: 44px;
    color: #ffffff;
    font-family: "Tinos", "Times New Roman", serif;
  }
  .services .lead { font-size: 16px; margin-bottom: 8px; }
  .services ul { list-style: none; }
  .services li {
    font-size: 14.5px; line-height: 1.5;
    display: flex; align-items: center; gap: 10px;
  }
  .services li::before {
    content: ""; width: 8px; height: 8px;
    background: var(--green); flex: none;
  }
</style>
</head>
<body>

  <section class="card front" aria-label="Business card front">
    <svg class="card-art" width="520" height="297" viewBox="0 0 520 297" aria-hidden="true">
      <defs>
        <linearGradient id="headshotTone" x1="0" y1="0" x2="1" y2="0">
          <stop offset="0" stop-color="#e8e6e2"/>
          <stop offset="0.45" stop-color="#c9a987"/>
          <stop offset="0.75" stop-color="#3a3532"/>
          <stop offset="1" stop-color="#1f1f1f"/>
        </linearGradient>
      </defs>
      <path d="M0 0 H520 V118 Q300 168 0 150 Z" fill="url(#headshotTone)"/>
      <path d="M0 150 Q300 168 520 118 V138 Q300 190 0 164 Z" fill="var(--navy)"/>
    </svg>
    <div class="headshot" role="img" aria-label="Headshot photo of Lena Marwick"></div>

    <div class="brand"><span class="mark-dot"></span>Marwick Insurance</div>

    <div class="agent">
      <p class="name">Lena Marwick</p>
      <p class="title">Independent Agent</p>
    </div>

    <div class="contact">
      <p>704-555-0182</p>
      <p>Lenamarwick@quillpost.example</p>
      <p>www.marwickInsurance.example</p>
    </div>
    <div class="accent-tab"></div>
  </section>

  <section class="card back" aria-label="Business card back">
    <svg class="card-art" width="520" height="297" viewBox="0 0 520 297" aria-hidden="true">
      <defs>
        <linearGradient id="backBlue" x1="0" y1="0" x2="1" y2="1">
          <stop offset="0" stop-color="var(--royal)"/>
          <stop offset="1" stop-color="var(--blue-deep)"/>
        </linearGradient>
      </defs>
      <path d="M230 0 H520 V297 H215 Q185 150 230 0 Z" fill="url(#backBlue)"/>
      <path d="M210 0 Q168 150 198 297" fill="none" stroke="var(--navy)" stroke-width="3"/>
    </svg>

    <div class="brand"><span class="mark-dot"></span>Marwick</div>

    <div class="services">
      <p class="lead">I can also help you with.....</p>
      <ul>
        <li>Long Term Care Insurance</li>
        <li>Fixed Annuities</li>
        <li>Life Insurance</li>
        <li>Medicare Supplement Insurance</li>
        <li>Individual Major Medical Insurance</li>
        <li>Final Expense Insurance</li>
        <li>Medicare Advantage Plans</li>
      </ul>
    </div>
  </section>

</body>
</html>
```